Web Design Project for starting CCTV/Camera security installer/reseller

Hello,

An old class mate is starting his own little CCTV/Camera security business as a one-man-gang.

He asked me to do his website but unfortunatly my design skills are not worth looking at :) The coding is no problem.

So I'm here to request a design.

What he wants is a site that lists the products he might install which is based on a small tree structure. So see it as a shop overview/display but without the baskets & cashout options.

you can find a site structure scheme, logo, product images & data sheet pdf's at this filebarn address:

https://www.filebarn.example/sh/kx7pq2931rv4zt8/wnLpHsRa3u/Vizor-Guard

the site itself is http://www.vizor-guard.example but only has a splash screen until I have a design for it.

the logo is a bit out of proportions, not sure if you can make something good out of it :/

Most content is in Dutch, I'll see if I can translate the needed parts...
Updates

Dear designers,

I have some good new for you.

You are allowed to use only that chrome Vizor-Guard part of the logo,
which should make things a lot easier to fit into your design ideas.

Keep up the creativity!

Dear designers,

I uploaded a new logo to the filebarn space.

It's a png but unfortunately it's not transparent, I'm still waiting for that one
but you know how to erase it in photoshop.

Target Market(s)

people looking for a visual solution to protect their company/home

Industry/Entity Type

Security

Requirements
Must have
• an iconized way to browse/display a tree. (not the traditional folder/explorer style)

maybe first a page with buttons/icons showing level 1 the group types (IP cams, IP servers, Accessories)

level 2 product groups (dome cam, ptz cam etc)

level 3 the actual product + a link to a pdf datasheet (if any)

could be multipage or maybe in/on-page since the product list won't be that huge.

maybe some random product info left and/or right so that the content area is not massive since he has not much to type
;)

```html
<!DOCTYPE html>
<html lang="en">
<head>
<meta charset="utf-8">
<title>Vizor-Guard — Camera Surveillance</title>
<link rel="stylesheet" href="https://fonts.googleapis.com/css2?family=Arimo:wght@400;700&family=Poppins:wght@600&family=Ubuntu:wght@400;500;700&display=swap">
<style>
:root{
  --blue-deep:#1a5793;
  --blue-mid:#1e6fc0;
  --blue-bright:#2d8ce4;
  --blue-accent:#1b62a8;
  --grey-bg:#e5e5e5;
  --grey-text:#444;
  --grey-rule:#c9c9c9;
  --black:#000;
  --footer-text:#e0e0e0;
  --bar-bg:#1b1b1b;
  --bar-text:#4a4a4a;
  --white:#fff;
}
*{margin:0;padding:0;box-sizing:border-box}
html,body{width:1200px;height:1180px;overflow:hidden}
body{position:relative;background:var(--black);font-family:"Arimo",Arial,sans-serif}
.abs{position:absolute}

.top{left:0;top:0;width:1200px;height:538px;
  background:radial-gradient(ellipse 700px 360px at 600px 330px,#2374c4 0%,var(--blue-deep) 70%,#164b80 100%)}
.masthead{left:75px;top:0;width:1050px;height:148px;
  background:linear-gradient(90deg,var(--blue-mid) 0%,var(--blue-bright) 45%,var(--blue-bright) 75%,var(--blue-mid) 100%);
  box-shadow:0 8px 14px rgba(0,0,0,.28)}

.brand{left:120px;top:34px;display:flex;align-items:center;gap:12px}
.brand-mark{width:56px;height:56px;border-radius:50%;background:var(--white);border:4px solid #4aa3ec}
.brand-name{font-family:"Ubuntu",sans-serif;font-weight:700;font-size:26px;color:var(--white)}

.phone{left:600px;top:19px;display:flex;align-items:center;gap:16px;
  font-family:"Ubuntu",sans-serif;font-weight:700;font-size:18px;color:var(--white);letter-spacing:.3px}
.search{left:830px;top:19px;width:250px;height:28px;background:#eef2f6;border:1px solid #cfd8e2;display:flex;justify-content:flex-end}
.search-btn{width:32px;height:26px;border-left:1px solid #d0d6dc;display:flex;align-items:center;justify-content:center}

.nav{left:421px;top:87px;display:flex;list-style:none;
  font-family:"Ubuntu",sans-serif;font-weight:700;font-size:13px;color:var(--white);letter-spacing:.2px}
.nav li{height:27px;line-height:27px}
.nav .current{background:var(--black);border-radius:14px;width:80px;text-align:center}

.slider{left:120px;top:172px;width:960px;height:344px;border:5px solid var(--white);
  background:radial-gradient(ellipse 520px 260px at 300px 110px,#4ea6ec 0%,#2b85dc 45%,#1c63bf 100%)}
.slide-title{left:0;top:66px;width:470px;text-align:center;font-family:"Poppins",sans-serif;font-weight:600;
  font-size:34px;line-height:60px;color:#0b0b0b;text-shadow:0 0 3px rgba(255,255,255,.55)}
.slide-copy{left:26px;top:206px;width:410px;font-size:14px;line-height:17px;color:var(--white)}
.slide-media{left:455px;top:15px;width:475px;height:270px;border-radius:8px;
  background:radial-gradient(ellipse at 55% 40%,#f2f4f6 0%,#cdd6df 35%,rgba(80,140,210,.0) 70%)}
.arrow{top:150px}

.intro{left:0;top:540px;width:1200px;height:312px;background:var(--grey-bg);border-bottom:2px dotted #6aa6e0}
.col h2{font-family:"Ubuntu",sans-serif;font-weight:400;font-size:21px;line-height:25px;color:#333}
.col h2 b{font-weight:700}
.col p{font-size:12px;line-height:18px;color:var(--grey-text);margin-top:18px}
.col p strong{color:#333}
.col .lead{margin-top:37px}
.divider{top:568px;width:1px;height:230px;background:var(--grey-rule)}

.more{display:flex;width:79px;height:23px}
.more span{flex:1;background:#a7bfd8;color:var(--blue-accent);font-family:"Ubuntu",sans-serif;font-weight:700;font-size:14px;line-height:23px;padding-left:6px}
.more i{width:22px;background:var(--blue-accent);display:flex;align-items:center;justify-content:center}

.info h3{font-family:"Arimo",sans-serif;font-weight:400;font-size:20px;line-height:24px;color:var(--white)}
.info h3 b{font-weight:700}
.info p{font-size:12px;line-height:18px;color:var(--footer-text);margin-top:24px}
.info p+p{margin-top:18px}
.info ul{list-style:none;margin:18px 0 0 13px;font-size:12px;line-height:18px;color:var(--footer-text)}
.fdiv{top:870px;width:1px;height:256px;background:#2a2a2a}

.bar{left:0;top:1140px;width:1200px;height:40px;background:var(--bar-bg);font-size:12px;color:var(--bar-text)}
.bar .copy{left:120px;top:12px}
.bar .links{right:121px;top:12px}
</style>
</head>
<body>
<div class="abs top"></div>
<div class="abs masthead"></div>

<div class="abs brand">
  <div class="brand-mark"></div>
  <div class="brand-name">Vizor-Guard</div>
</div>

<div class="abs phone">
  <svg width="22" height="30" viewBox="0 0 22 30" aria-hidden="true"><path d="M6 2 L10 9 L7 12 C8 17 11 21 14 23 L17 20 L21 25 L17 29 C8 27 2 16 3 5 Z" fill="#1b5793"/></svg>
  <span>(XXX) XXX - XXXX</span>
</div>
<div class="abs search"><div class="search-btn">
  <svg width="16" height="16" viewBox="0 0 16 16" aria-hidden="true"><circle cx="6.5" cy="6.5" r="5" fill="none" stroke="#9aa4ae" stroke-width="1.6"/><line x1="10" y1="10" x2="15" y2="15" stroke="#9aa4ae" stroke-width="2"/></svg>
</div></div>

<ul class="abs nav">
  <li class="current">HOME</li>
  <li style="margin-left:32px">ABOUT US</li>
  <li style="margin-left:47px">PRODUCTS</li>
  <li style="margin-left:47px">SERVICES</li>
  <li style="margin-left:47px">SUPPORT</li>
  <li style="margin-left:51px">CONTACT US</li>
</ul>

<div class="abs slider">
  <h1 class="abs slide-title">INFRARED AND NIGHT-<br>VISION CAMERAS</h1>
  <p class="abs slide-copy">Low profile infrared and night-vision cameras monitor your prop-erty 24 hours a day. Watch the kids in the backyard and the deliv-ery person at the front door on any TV or touchscreen in the home.</p>
  <div class="abs slide-media" role="img" aria-label="Two white bullet-style infrared security cameras on wall mounts"></div>
  <svg class="abs arrow" style="left:5px" width="22" height="30" viewBox="0 0 22 30" aria-hidden="true"><path d="M18 2 L5 15 L18 28" fill="none" stroke="#174f8c" stroke-width="5"/></svg>
  <svg class="abs arrow" style="left:925px" width="22" height="30" viewBox="0 0 22 30" aria-hidden="true"><path d="M4 2 L17 15 L4 28" fill="none" stroke="#174f8c" stroke-width="5"/></svg>
</div>

<section class="abs intro"></section>
<div class="abs col" style="left:120px;top:562px;width:475px">
  <h2>Welcome at <b>Vizor-Guard Camera surveilance</b></h2>
  <p class="lead"><strong>Are you looking for a camera system for your home or company?</strong></p>
  <p><strong>Then you are at Vizor-Guard at the right address!</strong></p>
  <p>We offer a large amount of surveilance camera's, video storage systems and surveilance monitors.</p>
  <p>But we also have complete camera surveillance sets for you (analogue or IP camera's) including the cables and power supplies, so that you don't have to worry about additional components when ordering.</p>
</div>
<div class="abs divider" style="left:600px"></div>
<div class="abs col" style="left:612px;top:562px;width:480px">
  <h2>Service <b>You can trust</b></h2>
  <p class="lead">Lorem ipsum dolor siamet, consectetur adipisicingelit, seddo eiusmod tempor incididunt ut laboreet dolore magnaaliqua. nimad minim veniam, quis nostrud exercitation ullamco laboris nisi ut aliquip eia commodo consequat.</p>
  <p>Duis aute irure dolor in reprehenderit in voluptate velit esse cillum dolor fugiat nulla paria-tur. Excepteur sint occaecat cupidatat li proident, sunilculpa&nbsp; officia deserunt mollit anim id est laborum.Duis aute irure dolor in reprehenderit in voluptate velit esse cillum dolore eu fugiat nulla pariatur. Excepteur sint occaecat cupidatat li proident, sunt in culpa qui officia deserunt mollit anim id est laborum.fugiat nulla pariatur. Excepteur sint occaecat cupidatat li proident, sunt in culpa qui officia deserunt mollit anim id est laborum.</p>
</div>
<a class="abs more" style="left:120px;top:810px"><span>MORE</span><i><svg width="8" height="10" viewBox="0 0 8 10" aria-hidden="true"><path d="M1 1 L6 5 L1 9" fill="none" stroke="#fff" stroke-width="2"/></svg></i></a>
<a class="abs more" style="left:611px;top:810px"><span>MORE</span><i><svg width="8" height="10" viewBox="0 0 8 10" aria-hidden="true"><path d="M1 1 L6 5 L1 9" fill="none" stroke="#fff" stroke-width="2"/></svg></i></a>

<div class="abs info" style="left:122px;top:869px;width:310px">
  <h3><b>OUR</b> PRODUCT</h3>
  <p>Lorem ipsum dolor siamet, consectetur adipisicingelit, seddo eiusmod tempor incididmagnaaliqua. nimad minim venLorem ipsum dolor siamet, consectetur adipisicingelit, seddo eiusmod tempor incididunt utre magnaimad minim ven</p>
  <ul><li>Dome Camera</li><li>Box Camera</li><li>IR Dome Camera</li><li>Speed Dome Camera</li><li>Standalone DVR</li></ul>
</div>
<div class="abs fdiv" style="left:437px"></div>
<div class="abs info" style="left:450px;top:869px;width:306px">
  <h3><b>OUR</b> SERVICES</h3>
  <p>Lorem ipsum dolor siamet, consectetur adipisicingelit, seddo eiusmod tempor incididmagnaaliqua. nimad minim venLorem ipsum dolor siamet, consectetur adipisicingelit, seddo eiusmod tempor incididunt utre magnaimad minim venLorem ipsum dolor siamet, consectetur adipisicingelit, seddo eiusmod tempor incididunt utre magnaimad minim ven</p>
  <ul style="margin-left:17px"><li>Analogue Cameras</li><li>IP Cameras</li></ul>
</div>
<div class="abs fdiv" style="left:762px"></div>
<div class="abs info" style="left:771px;top:869px;width:310px">
  <h3><b>OUR</b> SUPPORT</h3>
  <p>Lorem ipsum dolor siamet, consectetur adipisicingelit, seddo eiusmod tempor incididmagnaaliqua. nimad minim venLorem ipsum dolor siamet, consectetur adipisicingelit, seddo eiusmod tempor incididunt utre magnaimad minim ven</p>
  <p>venLorem ipsum dolor siamet, consectetur adipisicingelit, seddo eiusmod tempor incididunt utre magnaimad minim venvenLorem ipsum dolor siamet, consectetur adipisic-ingelit, seddo eiusmod tempor incididunt utre magnaimad minim ven</p>
</div>

<footer class="abs bar">
  <div class="abs copy">© 2012 Vizor-Guard.&nbsp; All Rights Reserved.</div>
  <div class="abs links">Home | About | Products | Services | Support | Contact Us</div>
</footer>
</body>
</html>
```